Tablet App design for business management system

TaskOra is a business management system made especially for service based businesses (our subscribers). It enables systemising your service businesses. This can be used by diverse industries like automotive service, beauty (hair salons, nail spas), Spas, Chiropractor, acupuntcure, osteo, yoga studio, business coach, etc.

The UI of the app needs to be designed using flat and clean UI design trends that are currently prevailing for B2C apps. Even the sliding menu panel can be removed and alternative placement of this functionality can be suggested. The color palette used for the design should be limited (3-5 colours)

The Current UI screens are open to suggestions for change. For ease of management in minimum steps, consolidation of functionality on different screens can be suggested, accompanies by a rational reason with the objective of having a simple and straight forward user experience.

User should be able to move from one function to another (booking > view appointments > profile) in no more than 1 or max 2 gestures.

Target Market(s)

SME businesses that provide time based services

Industry/Entity Type

Business

Font styles to use
Sans Serif

Requirements
Must have
• The power point slides give a detailed account of the process flow and functionality that the app is to follow.
• Reference this slide to ensure that your final design must have all screens that are required to deliver the functionality.

```html
<!DOCTYPE html>
<html lang="en">
<head>
<meta charset="utf-8">
<title>TaskOra – tablet business management screens</title>
<link rel="stylesheet" href="https://fonts.googleapis.com/css2?family=Roboto:wght@400;500;700&display=swap">
<style>
:root{
  --teal:#1fb3c8;
  --stage:#5b5d5f;
  --panel:#eeeeee;
  --band:#d7d7d7;
  --line:#e2e2e2;
  --ink:#222222;
  --muted:#7a7a7a;
  --white:#ffffff;
  --green:#3bb54a;
  --amber:#f0b429;
  --alert:#e8403f;
}
*{box-sizing:border-box;margin:0;padding:0}
html,body{width:1200px;height:909px;overflow:hidden;background:var(--stage);font-family:"Roboto",Arial,sans-serif;color:var(--ink)}
.screen{position:absolute;width:717px;height:538px;background:var(--white);transform:scale(.8);transform-origin:0 0;overflow:hidden}
.screen--checkout{left:16px;top:16px}
.screen--appointment{left:610px;top:16px}
.screen--payment{left:16px;top:462px;background:#ebebeb}
.screen--sent{left:610px;top:462px}
.a{position:absolute}
.topbar{position:absolute;left:0;top:0;width:717px;height:45px;background:var(--teal);color:var(--white)}
.topbar--light{background:var(--white);color:var(--ink)}
.status{position:absolute;top:2px;font-size:8px;font-weight:500}
.status--l{left:5px}.status--c{left:0;width:717px;text-align:center}.status--r{right:5px}
.battery{display:inline-block;width:16px;height:6px;background:currentColor;vertical-align:middle;margin-left:2px}
.title{position:absolute;left:0;top:21px;width:717px;text-align:center;font-size:12px;font-weight:500}
.back{position:absolute;left:11px;top:21px}
.sidebar{position:absolute;left:0;top:45px;width:210px;height:493px;background:var(--panel)}
.search{position:absolute;left:7px;top:7px;width:196px;height:28px;background:var(--white);border:1px solid #dcdcdc;font-size:11px;color:#9a9a9a;display:flex;align-items:center;justify-content:center;gap:6px}
.card{position:absolute;left:7px;width:196px;height:71px;background:var(--white);box-shadow:0 1px 1px rgba(0,0,0,.12)}
.card--active{background:var(--teal);color:var(--white)}
.card .avatar{left:10px;top:11px;width:36px;height:36px}
.card .name{position:absolute;left:56px;top:14px;font-size:12px;font-weight:500}
.card .svc{position:absolute;left:56px;top:29px;font-size:9.5px;white-space:nowrap;width:136px;overflow:hidden;text-overflow:ellipsis}
.card .staff{position:absolute;left:56px;top:49px;font-size:12px;display:flex;align-items:center;gap:5px}
.dot{display:inline-block;width:13px;height:13px;border-radius:50%;background:var(--green);border:2px solid var(--white);box-shadow:0 0 0 1px var(--green)}
.dot--amber{background:var(--amber);box-shadow:0 0 0 1px var(--amber)}
.card--active .dot{box-shadow:none}
.avatar{position:absolute;border-radius:50%;background:radial-gradient(circle at 50% 40%,#8a5a42,#3a2620)}
.avatar--men{background:radial-gradient(circle at 50% 40%,#6f6f72,#232325)}
.avatar--feature{background:radial-gradient(circle at 50% 45%,#9a5d3e,#c4343c 80%)}
.row{position:absolute;font-size:10.5px;display:flex;align-items:flex-start;gap:12px;line-height:16px}
.rule{position:absolute;height:1px;background:var(--line)}
.vrule{position:absolute;width:1px;background:var(--line)}
.band{position:absolute;height:30px;background:var(--band);font-size:12px;font-weight:500;display:flex;align-items:center;justify-content:center}
.icon{width:12px;height:12px;flex:none;margin-top:2px}
.placeholder{color:var(--muted)}
.ph{position:absolute;font-size:10.5px;color:var(--muted);line-height:16px}
.tabs{position:absolute;left:7px;top:11px;width:196px;height:20px;display:flex;font-size:8.5px}
.tabs span{flex:1;display:flex;align-items:center;justify-content:center;background:#d8d8d8;color:var(--white)}
.tabs span.on{background:var(--teal)}
.check{position:absolute;left:10px;font-size:10.5px;display:flex;align-items:center;gap:10px}
.tick{width:14px;height:14px;flex:none}
.field{position:absolute;height:28px;border:1px solid #dcdcdc;background:var(--white);font-size:10.5px;color:var(--muted);display:flex;align-items:center;justify-content:center}
.caps{position:absolute;left:0;font-size:10px;width:100%;text-align:center}
.btn{position:absolute;height:28px;background:var(--teal);color:var(--white);font-size:12px;font-weight:500;display:flex;align-items:center;justify-content:center}
.btn--ghost{background:var(--white);color:var(--teal);border:1px solid var(--teal)}
.note{position:absolute;left:14px;width:270px}
.note .who{font-size:11.5px;display:flex;align-items:center;gap:6px}
.note .svc{font-size:9.5px;margin-left:19px}
.note .stamp{font-size:7px;color:var(--muted);margin-left:19px}
.note .body{font-size:9px;font-style:italic;color:#444;margin:8px 0 0 19px;line-height:12.5px}
.sheet{position:absolute;background:var(--white);box-shadow:0 1px 2px rgba(0,0,0,.15)}
.cell{position:absolute;font-size:11.5px}
.head{font-weight:500}
.pill{position:absolute;height:20px;background:#e1e1e1;font-size:11.5px;display:flex;align-items:center;justify-content:center}
.opt{position:absolute;left:14px;font-size:11.5px;color:#555;display:flex;align-items:center;gap:9px}
.opt--on{color:var(--teal)}
.money{position:absolute;height:28px;border:1px solid #dcdcdc;font-size:11px;display:flex;align-items:center;padding:0 8px;justify-content:space-between}
.money i{font-style:normal;color:var(--muted)}
.label{position:absolute;font-size:11px;color:#444}
</style>
</head>
<body>

<section class="screen screen--checkout">
  <header class="topbar">
    <span class="status status--l">Tablet ◠</span><span class="status status--c">4:21 PM</span><span class="status status--r">✱ 100% <span class="battery"></span></span>
    <svg class="back" width="10" height="14" viewBox="0 0 10 14"><path d="M8 1 2 7l6 6" fill="none" stroke="#fff" stroke-width="2"/></svg>
    <div class="title">Check Out</div>
  </header>
  <aside class="sidebar">
    <div class="search"><svg width="11" height="11" viewBox="0 0 11 11"><circle cx="4.5" cy="4.5" r="3.6" fill="none" stroke="#9a9a9a"/><path d="M7.2 7.2 10 10" stroke="#9a9a9a"/></svg>Search Customer</div>
    <div class="card" style="top:42px"><div class="avatar" role="img" aria-label="Customer portrait"></div><div class="name">Adela Moreno</div><div class="svc">Haircut, Hairstyling, Pedicure, Manicure</div><div class="staff"><span class="dot"></span>Kat &amp; Kate</div></div>
    <div class="card card--active" style="top:119px"><div class="avatar avatar--feature" role="img" aria-label="Customer portrait"></div><div class="name">Nadia Lynn Harlow</div><div class="svc">Haircut, Pedicure, Manicure</div><div class="staff"><span class="dot"></span>Romeo &amp; Juliet</div></div>
    <div class="card" style="top:196px"><div class="avatar avatar--men" role="img" aria-label="Customer portrait"></div><div class="name">Carter Dunmore</div><div class="svc">Haircut, Massage</div><div class="staff"><span class="dot"></span>Marisol</div></div>
  </aside>
  <div class="a" style="left:210px;top:45px;width:297px;height:493px">
    <div class="avatar avatar--feature" style="left:119px;top:28px;width:70px;height:70px" role="img" aria-label="Customer portrait"></div>
    <div class="a" style="left:0;top:110px;width:297px;text-align:center;font-size:12px;font-weight:500">Nadia Lynn Harlow</div>
    <div class="row" style="left:14px;top:140px"><svg class="icon" viewBox="0 0 12 12"><path d="M2 1h3l1 3-2 1a7 7 0 0 0 3 3l1-2 3 1v3c-6 0-10-4-10-10z" fill="#999"/></svg>+63 900 555 0142</div>
    <div class="rule" style="left:0;top:163px;width:297px"></div>
    <div class="row" style="left:14px;top:170px"><svg class="icon" viewBox="0 0 12 12"><rect x="1" y="3" width="10" height="7" fill="#999"/><path d="M1 3l5 4 5-4" fill="none" stroke="#fff"/></svg>nl_harlow@mailbox.test</div>
    <div class="rule" style="left:0;top:193px;width:297px"></div>
    <div class="row" style="left:14px;top:200px"><svg class="icon" viewBox="0 0 12 12"><rect x="1" y="6" width="10" height="5" fill="#999"/><rect x="5.5" y="2" width="1" height="4" fill="#999"/></svg>02 Oct 1976</div>
    <div class="rule" style="left:0;top:223px;width:297px"></div>
    <div class="row" style="left:14px;top:230px"><svg class="icon" viewBox="0 0 12 12"><path d="M6 11S2 7 2 4.5a4 4 0 0 1 8 0C10 7 6 11 6 11z" fill="#999"/></svg><span>Linden St., Maple Heights<br>Riverton<br>MO 9000</span></div>
    <div class="band" style="left:0;top:283px;width:297px">Notes</div>
    <div class="note" style="top:323px"><div class="who"><span class="dot"></span>Romeo &amp; Juliet</div><div class="svc">Haircut, Pedicure, Manicure</div><div class="stamp">15 Nov 2015 AT 11:45 AM</div><div class="body">Lorem ipsum dolor sit amet, consectetur adipiscing elit. Vestibulum dolor elit, mattis non quam sed, sodales vestibulum justo.</div></div>
    <div class="rule" style="left:0;top:422px;width:297px"></div>
    <div class="note" style="top:432px"><div class="who"><span class="dot dot--amber"></span>Marisol</div><div class="svc">Haircut, Massage</div><div class="stamp">16 Nov 2015 AT 07:28 AM</div><div class="body">Lorem ipsum dolor sit amet, consectetur adipiscing elit. Vestibulum dolor elit, mattis non quam sed, so-</div></div>
  </div>
  <div class="a" style="left:507px;top:45px;width:210px;height:493px;border-left:1px solid var(--line)">
    <div class="tabs"><span class="on">Services</span><span>Classes</span></div>
    <div class="check" style="top:49px"><svg class="tick" viewBox="0 0 14 14"><circle cx="7" cy="7" r="6" fill="none" stroke="#1fb3c8"/><path d="M4 7l2 2 4-4" fill="none" stroke="#1fb3c8"/></svg>Pedicure</div>
    <div class="check" style="top:77px"><svg class="tick" viewBox="0 0 14 14"><circle cx="7" cy="7" r="6" fill="none" stroke="#1fb3c8"/><path d="M4 7l2 2 4-4" fill="none" stroke="#1fb3c8"/></svg>Haircut</div>
    <div class="check" style="top:105px"><svg class="tick" viewBox="0 0 14 14"><circle cx="7" cy="7" r="6" fill="none" stroke="#1fb3c8"/><path d="M4 7l2 2 4-4" fill="none" stroke="#1fb3c8"/></svg>Manicure</div>
    <div class="check" style="top:133px"><svg class="tick" viewBox="0 0 14 14"><circle cx="7" cy="7" r="6" fill="none" stroke="#1fb3c8"/><path d="M4 7l2 2 4-4" fill="none" stroke="#1fb3c8"/></svg>Massage</div>
    <div class="band" style="left:-1px;top:163px;width:211px">Next Booking</div>
    <div class="row" style="left:14px;top:200px"><svg class="icon" viewBox="0 0 12 12"><rect x="1" y="2" width="10" height="9" fill="none" stroke="#999"/><rect x="1" y="2" width="10" height="2" fill="#999"/></svg>20 Nov 2015</div>
    <div class="rule" style="left:0;top:223px;width:210px"></div>
    <div class="row" style="left:14px;top:230px"><svg class="icon" viewBox="0 0 12 12"><circle cx="6" cy="6" r="5.5" fill="#999"/><circle cx="6" cy="5" r="2" fill="#fff"/></svg>Marisol</div>
    <div class="rule" style="left:0;top:253px;width:210px"></div>
    <div class="row" style="left:14px;top:260px"><svg class="icon" viewBox="0 0 12 12"><circle cx="6" cy="6" r="4" fill="none" stroke="#999" stroke-width="3" stroke-dasharray="2 1.2"/></svg><span>Massage<br>Hair Rebonding<br>Foot Spa</span></div>
    <div class="rule" style="left:0;top:313px;width:210px"></div>
    <div class="caps" style="top:326px">OR CHOOSE MANUALLY</div>
    <div class="field" style="left:14px;top:343px;width:182px">Select a Service/Class <span style="margin-left:22px;font-size:7px">▼</span></div>
    <div class="caps" style="top:383px">DUE IN</div>
    <div class="field" style="left:14px;top:400px;width:84px"># of Weeks</div>
    <div class="field" style="left:112px;top:400px;width:84px"># of Days</div>
    <div class="btn" style="left:14px;top:451px;width:182px">Next</div>
  </div>
</section>

<section class="screen screen--appointment">
  <header class="topbar">
    <span class="status status--l">Tablet ◠</span><span class="status status--c">4:21 PM</span><span class="status status--r">✱ 100% <span class="battery"></span></span>
    <svg class="back" width="10" height="14" viewBox="0 0 10 14"><path d="M8 1 2 7l6 6" fill="none" stroke="#fff" stroke-width="2"/></svg>
    <div class="title">Add an Appointment</div>
  </header>
  <aside class="sidebar">
    <div class="search"><svg width="11" height="11" viewBox="0 0 11 11"><circle cx="4.5" cy="4.5" r="3.6" fill="none" stroke="#9a9a9a"/><path d="M7.2 7.2 10 10" stroke="#9a9a9a"/></svg>Search Customer</div>
    <div class="card" style="top:42px"><div class="avatar" role="img" aria-label="Customer portrait"></div><div class="name">Adela Moreno</div><div class="svc">Haircut, Hairstyling, Pedicure, Manicure</div><div class="staff"><span class="dot"></span>Kat &amp; Kate</div></div>
    <div class="card" style="top:119px"><div class="avatar avatar--feature" role="img" aria-label="Customer portrait"></div><div class="name">Nadia Lynn Harlow</div><div class="svc">Haircut, Pedicure, Manicure</div><div class="staff"><span class="dot"></span>Romeo &amp; Juliet</div></div>
    <div class="card" style="top:196px"><div class="avatar avatar--men" role="img" aria-label="Customer portrait"></div><div class="name">Carter Dunmore</div><div class="svc">Haircut, Massage</div><div class="staff"><span class="dot"></span>Marisol</div></div>
  </aside>
  <div class="a" style="left:210px;top:45px;width:297px;height:493px">
    <svg class="a" style="left:16px;top:17px" width="72" height="72" viewBox="0 0 72 72"><circle cx="36" cy="36" r="35" fill="#bdbdbd" stroke="#e6e6e6" stroke-width="2"/><circle cx="36" cy="27" r="11" fill="#fff"/><path d="M14 60a22 18 0 0 1 44 0z" fill="#fff"/><rect x="28" y="47" width="16" height="11" rx="2" fill="#bdbdbd"/><circle cx="36" cy="52.5" r="3" fill="#fff"/></svg>
    <div class="row placeholder" style="left:104px;top:27px"><svg class="icon" viewBox="0 0 12 12"><circle cx="6" cy="4" r="2.5" fill="#aaa"/><path d="M1.5 11a4.5 4 0 0 1 9 0z" fill="#aaa"/></svg>first name</div>
    <div class="rule" style="left:122px;top:50px;width:175px"></div>
    <div class="row placeholder" style="left:104px;top:57px"><svg class="icon" viewBox="0 0 12 12"><circle cx="6" cy="4" r="2.5" fill="#aaa"/><path d="M1.5 11a4.5 4 0 0 1 9 0z" fill="#aaa"/></svg>last name</div>
    <div class="rule" style="left:122px;top:80px;width:175px"></div>
    <div class="row placeholder" style="left:14px;top:110px"><svg class="icon" viewBox="0 0 12 12"><path d="M2 1h3l1 3-2 1a7 7 0 0 0 3 3l1-2 3 1v3c-6 0-10-4-10-10z" fill="#aaa"/></svg>phone number</div>
    <div class="rule" style="left:0;top:133px;width:297px"></div>
    <div class="row placeholder" style="left:14px;top:140px"><svg class="icon" viewBox="0 0 12 12"><rect x="1" y="3" width="10" height="7" fill="#aaa"/><path d="M1 3l5 4 5-4" fill="none" stroke="#fff"/></svg>email address</div>
    <div class="rule" style="left:0;top:163px;width:297px"></div>
    <div class="row placeholder" style="left:14px;top:170px"><svg class="icon" viewBox="0 0 12 12"><rect x="1" y="6" width="10" height="5" fill="#aaa"/><rect x="5.5" y="2" width="1" height="4" fill="#aaa"/></svg>month</div>
    <div class="ph" style="left:107px;top:170px;font-size:7px">▼</div>
    <div class="vrule" style="left:122px;top:163px;height:30px"></div>
    <div class="ph" style="left:134px;top:170px">date</div><div class="ph" style="left:193px;top:170px;font-size:7px">▼</div>
    <div class="vrule" style="left:210px;top:163px;height:30px"></div>
    <div class="ph" style="left:220px;top:170px">year</div><div class="ph" style="left:280px;top:170px;font-size:7px">▼</div>
    <div class="rule" style="left:0;top:193px;width:297px"></div>
    <div class="row placeholder" style="left:14px;top:200px"><svg class="icon" viewBox="0 0 12 12"><path d="M6 11S2 7 2 4.5a4 4 0 0 1 8 0C10 7 6 11 6 11z" fill="#aaa"/></svg>address line 1</div>
    <div class="rule" style="left:0;top:223px;width:297px"></div>
    <div class="ph" style="left:38px;top:230px">address line 2</div>
    <div class="rule" style="left:0;top:253px;width:297px"></div>
    <div class="ph" style="left:38px;top:260px">suburb</div>
    <div class="vrule" style="left:210px;top:253px;height:30px"></div>
    <div class="ph" style="left:220px;top:260px">postal code</div>
    <div class="band" style="left:0;top:283px;width:297px">Notes</div>
  </div>
  <div class="a" style="left:507px;top:45px;width:210px;height:493px;border-left:1px solid var(--line)">
    <div class="tabs"><span class="on">Services</span><span>Classes</span></div>
    <div class="check" style="top:49px"><svg class="tick" viewBox="0 0 14 14"><circle cx="7" cy="7" r="6" fill="none" stroke="#888"/><path d="M4 7l2 2 4-4" fill="none" stroke="#888"/></svg>Pedicure</div>
    <div class="check" style="top:77px"><svg class="tick" viewBox="0 0 14 14"><circle cx="7" cy="7" r="6" fill="none" stroke="#888"/><path d="M4 7l2 2 4-4" fill="none" stroke="#888"/></svg>Haircut</div>
    <div class="check" style="top:105px"><svg class="tick" viewBox="0 0 14 14"><circle cx="7" cy="7" r="6" fill="none" stroke="#1fb3c8"/><path d="M4 7l2 2 4-4" fill="none" stroke="#1fb3c8"/></svg>Manicure</div>
    <div class="check" style="top:133px"><svg class="tick" viewBox="0 0 14 14"><circle cx="7" cy="7" r="6" fill="none" stroke="#888"/><path d="M4 7l2 2 4-4" fill="none" stroke="#888"/></svg>Massage</div>
    <div class="band" style="left:-1px;top:163px;width:211px">Next Booking</div>
    <div class="btn" style="left:14px;top:451px;width:182px">Save Appointment</div>
  </div>
</section>

<section class="screen screen--payment">
  <header class="topbar">
    <span class="status status--l">Tablet ◠</span><span class="status status--c">4:21 PM</span><span class="status status--r">✱ 100% <span class="battery"></span></span>
    <svg class="back" width="10" height="14" viewBox="0 0 10 14"><path d="M8 1 2 7l6 6" fill="none" stroke="#fff" stroke-width="2"/></svg>
    <div class="title">Payment</div>
  </header>
  <div class="sheet" style="left:14px;top:58px;width:689px;height:172px">
    <div class="cell head" style="left:38px;top:10px">SERVICES</div>
    <div class="cell head" style="left:195px;top:10px">PRICE LIST</div>
    <svg class="a" style="left:372px;top:9px" width="14" height="14" viewBox="0 0 14 14"><circle cx="7" cy="7" r="7" fill="#1fb3c8"/><path d="M4 7l2 2 4-4" fill="none" stroke="#fff" stroke-width="1.5"/></svg>
    <div class="cell head" style="left:392px;top:10px">DISCOUNTS</div>
    <div class="cell head" style="left:585px;top:10px">SUB-TOTAL</div>
    <div class="rule" style="left:0;top:32px;width:689px"></div>
    <div class="cell" style="left:20px;top:43px">Haircut</div><div class="cell" style="left:231px;top:43px">90</div><div class="pill" style="left:376px;top:39px;width:34px">$ 10</div><div class="pill" style="left:425px;top:39px;width:35px">0%</div><div class="cell" style="left:622px;top:43px">80</div>
    <div class="rule" style="left:0;top:67px;width:689px"></div>
    <div class="cell" style="left:20px;top:78px">Pedicure</div><div class="cell" style="left:231px;top:78px">20</div><div class="pill" style="left:376px;top:74px;width:34px">$ 0</div><div class="pill" style="left:425px;top:74px;width:35px">10%</div><div class="cell" style="left:622px;top:78px">18</div>
    <div class="rule" style="left:0;top:102px;width:689px"></div>
    <div class="cell" style="left:20px;top:113px">Manicure</div><div class="cell" style="left:231px;top:113px">20</div><div class="pill" style="left:376px;top:109px;width:34px">$ 0</div><div class="pill" style="left:425px;top:109px;width:35px">0%</div><div class="cell" style="left:622px;top:113px">20</div>
    <div class="rule" style="left:0;top:137px;width:689px"></div>
    <div class="cell head" style="left:20px;top:148px">Total</div><div class="cell head" style="left:214px;top:148px">$ 130</div><div class="cell head" style="left:606px;top:148px">$ 118</div>
  </div>
  <div class="sheet" style="left:14px;top:258px;width:689px;height:210px">
    <div class="cell head" style="left:0;top:9px;width:689px;text-align:center">PAYMENT METHOD</div>
    <div class="opt opt--on" style="top:31px"><svg width="14" height="14" viewBox="0 0 14 14"><circle cx="7" cy="7" r="7" fill="#1fb3c8"/><path d="M4 7l2 2 4-4" fill="none" stroke="#fff" stroke-width="1.5"/></svg>CASH</div>
    <div class="opt" style="top:62px"><svg width="14" height="14" viewBox="0 0 14 14"><circle cx="7" cy="7" r="6" fill="none" stroke="#888"/><path d="M4 7l2 2 4-4" fill="none" stroke="#888"/></svg>CREDIT CARD</div>
    <div class="opt" style="top:93px"><svg width="14" height="14" viewBox="0 0 14 14"><circle cx="7" cy="7" r="6" fill="none" stroke="#888"/><path d="M4 7l2 2 4-4" fill="none" stroke="#888"/></svg>EFTPOS</div>
    <div class="rule" style="left:16px;top:167px;width:180px"></div>
    <div class="opt" style="top:181px"><svg width="14" height="14" viewBox="0 0 14 14"><circle cx="7" cy="7" r="6" fill="none" stroke="#888"/><path d="M4 7l2 2 4-4" fill="none" stroke="#888"/></svg>CREDIT TO ACCOUNT</div>
    <div class="a" style="left:211px;top:31px;width:464px;height:164px;border:1px solid var(--line)">
      <div class="label" style="left:34px;top:21px">AMOUNT</div>
      <div class="money" style="left:87px;top:13px;width:84px"><i>$</i>100.00</div>
      <div class="label" style="left:291px;top:21px">CHANGE</div>
      <div class="money" style="left:344px;top:13px;width:84px"><i>$</i>0.00</div>
      <div class="a" style="left:-1px;top:55px;width:464px;height:30px;background:var(--alert);color:var(--white);font-size:12px;font-weight:500;display:flex;align-items:center;justify-content:center">BALANCE: $ 18.00</div>
      <div class="label" style="left:156px;top:101px">PAY WITH</div>
      <div class="money" style="left:208px;top:93px;width:123px;font-size:12px">EFTPOS<i style="font-size:7px">▼</i></div>
      <div class="label" style="left:34px;top:136px">AMOUNT</div>
      <div class="money" style="left:87px;top:128px;width:84px"><i>$</i>20.00</div>
      <div class="label" style="left:291px;top:136px">CHANGE</div>
      <div class="money" style="left:344px;top:128px;width:84px"><i>$</i>2.00</div>
    </div>
  </div>
  <div class="btn" style="left:267px;top:489px;width:182px">Confirm Payment</div>
</section>

<section class="screen screen--sent">
  <header class="topbar topbar--light">
    <span class="status status--l">Tablet ◠</span><span class="status status--c">4:21 PM</span><span class="status status--r">✱ 100% <span class="battery"></span></span>
  </header>
  <div class="a" style="left:307px;top:67px;width:115px;height:110px;border-radius:40% 40% 30% 30%;background:linear-gradient(135deg,#b98a6a 0%,#e8b92a 55%,#3a72c9 100%)" role="img" aria-label="Money bag, coins and card with a green tick"></div>
  <div class="a" style="left:0;top:185px;width:717px;text-align:center;font-size:12px;font-weight:700">Payment Sent!</div>
  <div class="a" style="left:0;top:213px;width:717px;text-align:center;font-size:11.5px;line-height:15px">Thank you Nadia. We have received<br>your payment.</div>
  <div class="rule" style="left:178px;top:271px;width:360px"></div>
  <div class="a" style="left:247px;top:303px;width:223px;height:139px;border:1px solid var(--line)">
    <div class="band" style="left:-1px;top:-1px;width:223px;font-size:11.5px">NEXT BOOKING</div>
    <div class="row" style="left:13px;top:40px;font-size:10px"><svg class="icon" viewBox="0 0 12 12"><rect x="1" y="2" width="10" height="9" fill="none" stroke="#999"/><rect x="1" y="2" width="10" height="2" fill="#999"/></svg>20 Nov 2015</div>
    <div class="row" style="left:13px;top:70px;font-size:10px"><svg class="icon" viewBox="0 0 12 12"><circle cx="6" cy="6" r="5.5" fill="#999"/><circle cx="6" cy="5" r="2" fill="#fff"/></svg>Marisol</div>
    <div class="row" style="left:13px;top:100px;font-size:10px"><svg class="icon" viewBox="0 0 12 12"><circle cx="6" cy="6" r="4" fill="none" stroke="#999" stroke-width="3" stroke-dasharray="2 1.2"/></svg>Massage, Hair Rebonding, Foot Spa</div>
  </div>
  <div class="btn btn--ghost" style="left:169px;top:474px;width:182px">Book Later</div>
  <div class="btn" style="left:365px;top:474px;width:182px">Book Now</div>
</section>

</body>
</html>
```